Summit & Compass Flyer

2023 Summit & Compass
Military, Veterans, Law Enforcement & Fire Fighters
Receive $300* Off Purchased Materials
*$300 maximum discount per order. $3,000 order minimum. Redeem up to 3 times per year.
Terms & Conditions: This program is intended for the professional contractor that supports Ridgewren Supply with material purchases. One-time purchasers and institutions are not eligible for this program. By choosing to participate, you represent to Ridgewren Supply that your participation is not prohibited by law. Ridgewren Supply reserves the right to cancel, suspend, and/or modify this promotion at any time, for any reason, without prior notice. Employees at Ridgewren Supply are not eligible to participate. All rights reserved by Ridgewren Supply. Promotion expires December 31, 2023.
Please use our 2023 logo - attached
I'm also attaching the 2022 flyer as an example but looking for a refreshed design!

```html
<!DOCTYPE html>
<html lang="en">
<head>
<meta charset="utf-8">
<title>Summit &amp; Compass Flyer</title>
<link rel="stylesheet" href="https://fonts.googleapis.com/css2?family=Oswald:wght@400;500;600&family=Montserrat:wght@600;700;800&family=Roboto:wght@400;700&display=swap">
<style>
  :root {
    --paper: #ffffff;
    --navy: #1f3e7c;
    --navy-deep: #1a3470;
    --navy-light: #2c4f94;
    --ink-light: #ffffff;
    --ink-muted: #c9d4ea;
    --pill-text: #22377a;
  }
  html, body {
    margin: 0;
    padding: 0;
    width: 953px;
    height: 1200px;
    overflow: hidden;
    background: var(--paper);
  }
  .canvas {
    position: relative;
    width: 953px;
    height: 1200px;
    background: var(--paper);
    overflow: hidden;
  }
  .flyer {
    position: absolute;
    left: 38px;
    top: 33px;
    width: 877px;
    height: 1127px;
    background: linear-gradient(180deg, var(--navy) 0%, var(--navy-light) 60%, var(--navy-deep) 100%);
    overflow: hidden;
  }
  .hero-tiles {
    position: absolute;
    left: 0;
    top: 0;
    width: 877px;
    height: 1127px;
  }
  .brand-mark {
    position: absolute;
    left: 0;
    width: 877px;
    top: 548px;
    text-align: center;
    font-family: "Oswald", sans-serif;
    font-weight: 500;
    font-size: 36px;
    letter-spacing: 2px;
    color: var(--ink-light);
    text-transform: uppercase;
  }
  .headline {
    position: absolute;
    left: 0;
    width: 877px;
    top: 674px;
    margin: 0;
    text-align: center;
    font-family: "Oswald", sans-serif;
    font-weight: 500;
    font-size: 56px;
    line-height: 1;
    color: var(--ink-light);
    text-transform: uppercase;
  }
  .audience {
    position: absolute;
    left: 0;
    width: 877px;
    top: 740px;
    margin: 0;
    text-align: center;
    font-family: "Oswald", sans-serif;
    font-weight: 500;
    font-size: 22px;
    letter-spacing: 0.6px;
    color: var(--ink-light);
    text-transform: uppercase;
  }
  .offer {
    position: absolute;
    left: 0;
    width: 877px;
    top: 772px;
    margin: 0;
    text-align: center;
    font-family: "Oswald", sans-serif;
    font-weight: 500;
    font-size: 124px;
    line-height: 1.15;
    color: var(--ink-light);
    text-transform: uppercase;
    transform: scaleX(0.84);
    transform-origin: center;
  }
  .offer .offer-off {
    font-size: 56px;
    margin-left: -6px;
  }
  .offer-pill {
    position: absolute;
    left: 221px;
    top: 909px;
    width: 420px;
    height: 42px;
    border-radius: 21px;
    background: var(--paper);
    color: var(--pill-text);
    font-family: "Montserrat", sans-serif;
    font-weight: 800;
    font-size: 25px;
    line-height: 42px;
    text-align: center;
    text-transform: uppercase;
  }
  .fine-print {
    position: absolute;
    left: 0;
    width: 877px;
    top: 966px;
    margin: 0;
    text-align: center;
    font-family: "Montserrat", sans-serif;
    font-weight: 700;
    font-size: 14.6px;
    color: var(--ink-light);
  }
  .terms {
    position: absolute;
    left: 28px;
    width: 820px;
    top: 998px;
    margin: 0;
    font-family: "Roboto", sans-serif;
    font-weight: 400;
    font-size: 10.6px;
    line-height: 1.42;
    color: var(--ink-muted);
  }
  .social {
    position: absolute;
    right: 42px;
    top: 1064px;
    display: flex;
    align-items: center;
    gap: 6px;
    font-family: "Montserrat", sans-serif;
    font-weight: 700;
    font-size: 14px;
    color: var(--ink-light);
  }
  .social-label {
    margin-right: 14px;
  }
  .social-square {
    width: 24px;
    height: 24px;
    border-radius: 4px;
    background: var(--ink-light);
    opacity: 0.85;
  }
</style>
</head>
<body>
<div class="canvas">
  <section class="flyer">
    <svg class="hero-tiles" viewBox="0 0 877 1127" xmlns="http://www.w3.org/2000/svg">
      <defs>
        <radialGradient id="tile-police" cx="0.45" cy="0.45" r="0.7">
          <stop offset="0" stop-color="#6b7078"/>
          <stop offset="0.45" stop-color="#3f444b"/>
          <stop offset="0.8" stop-color="#25282d"/>
          <stop offset="1" stop-color="#5a4a40"/>
        </radialGradient>
        <radialGradient id="tile-family" cx="0.5" cy="0.7" r="0.6">
          <stop offset="0" stop-color="#8d8c76"/>
          <stop offset="0.5" stop-color="#6f7563"/>
          <stop offset="0.85" stop-color="#9a8069"/>
          <stop offset="1" stop-color="#7d6553"/>
        </radialGradient>
        <radialGradient id="tile-fire" cx="0.3" cy="0.25" r="0.8">
          <stop offset="0" stop-color="#f4b23c"/>
          <stop offset="0.3" stop-color="#e46a22"/>
          <stop offset="0.6" stop-color="#b5391a"/>
          <stop offset="0.8" stop-color="#d9a634"/>
          <stop offset="1" stop-color="#4a3a2e"/>
        </radialGradient>
      </defs>
      <polygon role="img" aria-label="Photo: police officers in riot gear"
        points="192,120 442,370 192,620 -58,370"
        fill="url(#tile-police)" stroke="var(--paper)" stroke-width="6"/>
      <polygon role="img" aria-label="Photo: firefighters spraying water at a blaze"
        points="679,133 916,370 679,607 442,370"
        fill="url(#tile-fire)" stroke="var(--paper)" stroke-width="6"/>
      <polygon role="img" aria-label="Photo: soldier hugging a child holding a small US flag"
        points="443,-151 700,106 443,363 186,106"
        fill="url(#tile-family)" stroke="var(--paper)" stroke-width="6"/>
    </svg>

    <div class="brand-mark">Ridgewren Supply</div>

    <h1 class="headline">2023 Summit &amp; Compass</h1>
    <p class="audience">Military, Veterans, Law Enforcement &amp; Fire Fighters</p>
    <p class="offer">Receive $300 <span class="offer-off">Off</span></p>
    <div class="offer-pill">Purchased Materials</div>

    <p class="fine-print">*$300 maximum discount per order. $3,000 order minimum. Redeem up to 3 times per year.</p>
    <p class="terms">Terms &amp; Conditions: This program is intended for the professional contractor that supports Ridgewren Supply with material purchases. One-time purchasers and institutions are not eligible for this program. By choosing to participate, you represent to Ridgewren Supply that your participation is not prohibited by law. Ridgewren Supply reserves the right to cancel, suspend, and/or modify this promotion at any time, for any reason, without prior notice. Employees at Ridgewren Supply are not eligible to participate. All rights reserved by Ridgewren Supply. Promotion expires December 31, 2023.</p>

    <div class="social">
      <span class="social-label">Follow Us @ridgewrensupply</span>
      <span class="social-square"></span>
      <span class="social-square"></span>
      <span class="social-square"></span>
    </div>
  </section>
</div>
</body>
</html>
```